Postcard Design Project

Company Name - Rowan Office Goods LLC We service and Repair printers, Fax and Copiers and sells all Business Technology supplies including supplies for Printers and Copiers to all NYC Metropolitan area.

Target Market(s)

NYC Small to Medium size business

Industry/Entity Type

Business

Font styles to use
Sans Serif

Colors

Designer to choose colors to be used in the design.

Requirements
Must have
• Printer Repairs and Toners Sales

```html
<!DOCTYPE html>
<html lang="en">
<head>
<meta charset="utf-8">
<title>Rowan Office Goods LLC – Postcard</title>
<link rel="stylesheet" href="https://fonts.googleapis.com/css2?family=Bebas+Neue&family=Barlow:wght@700;800&family=Lato:wght@700;900&display=swap">
<style>
  :root {
    --page: #ececec;
    --blue-deep: #0a6db7;
    --blue-head: #1f62a8;
    --blue-wave: #29b6e8;
    --sky-top: #bfe2f7;
    --yellow: #fcd232;
    --yellow-bright: #f2ec1c;
    --ink: #2d2d2f;
    --white: #ffffff;
    --photo-a: #c9c9cb;
    --photo-b: #55585d;
    --stamp: #3a3a3c;
  }
  * { margin: 0; padding: 0; box-sizing: border-box; }
  html, body { width: 971px; height: 1200px; overflow: hidden; background: var(--page); }
  body { position: relative; font-family: "Lato", sans-serif; }

  .card { position: absolute; left: 81px; width: 809px; height: 538px; overflow: hidden; background: var(--white); }
  .card--front { top: 53px; background: linear-gradient(var(--sky-top), var(--white) 40%); }
  .card--back { top: 608px; }
  .card svg.art { position: absolute; left: 0; top: 0; }
  .abs { position: absolute; white-space: nowrap; }

  .display { font-family: "Barlow", sans-serif; font-weight: 800; }

  .headline { left: 38px; top: 22px; font-family: "Bebas Neue", sans-serif; font-weight: 400; font-size: 116px; line-height: 1; color: var(--blue-head); }
  .badge-text { left: 470px; top: 158px; width: 270px; text-align: center; font-family: "Barlow", sans-serif; font-weight: 800; font-size: 22px; line-height: 1.05; color: var(--ink); text-transform: uppercase; white-space: normal; }
  .promo { font-weight: 700; font-size: 26px; line-height: 1.15; }
  .promo--front { left: 38px; top: 248px; color: var(--yellow); }
  .promo--back { left: 31px; top: 268px; color: var(--blue-deep); }
  .call-label { font-size: 22px; line-height: 1; text-transform: uppercase; }
  .call-label--front { left: 38px; top: 331px; color: var(--blue-deep); }
  .call-label--back { left: 31px; top: 350px; color: var(--ink); }
  .phone { font-size: 62px; line-height: 1; letter-spacing: -0.5px; }
  .phone--front { left: 36px; top: 355px; color: var(--blue-deep); }
  .phone--back { left: 29px; top: 373px; color: var(--ink); }
  .visit-label { left: 38px; top: 438px; font-size: 27px; line-height: 1; color: var(--ink); }
  .web { left: 37px; top: 468px; font-size: 40px; line-height: 1; color: var(--blue-deep); }

  .brand { display: flex; align-items: center; gap: 10px; font-weight: 900; font-size: 18px; color: var(--ink); }
  .brand__mark { width: 24px; height: 24px; background: var(--blue-deep); flex: none; }
  .brand--front { left: 536px; top: 462px; }
  .brand--back { left: 475px; top: 236px; font-size: 20px; }

  .stamp { left: 674px; top: 45px; width: 89px; height: 89px; background: var(--stamp); }
  .address-line { left: 466px; width: 298px; height: 1px; background: var(--ink); }
  .footer-band { left: 0; top: 454px; width: 809px; height: 84px; background: var(--blue-deep); border-top: 5px solid var(--yellow); display: flex; align-items: center; justify-content: center; font-size: 34px; color: var(--white); }
</style>
</head>
<body>

<section class="card card--front">
  <svg class="art" width="809" height="538" viewBox="0 0 809 538">
    <defs>
      <linearGradient id="photoTone" x1="0" y1="0" x2="1" y2="1">
        <stop offset="0" stop-color="var(--photo-a)"/>
        <stop offset="1" stop-color="var(--photo-b)"/>
      </linearGradient>
    </defs>
    <path d="M0,178 C120,140 220,215 330,200 C440,186 560,140 809,150 L809,425 L0,425 Z" fill="var(--blue-wave)"/>
    <path d="M0,196 C120,158 220,233 330,218 C440,204 560,158 809,168 L809,425 L0,425 Z" fill="var(--blue-deep)"/>
    <rect x="0" y="321" width="540" height="104" fill="var(--yellow)"/>
    <g role="img" aria-label="Photo of an opened printer being repaired, with a multimeter beside it">
      <path d="M430,205 C560,170 660,160 809,168 L809,425 L530,425 C480,425 455,395 445,350 Z" fill="url(#photoTone)"/>
    </g>
    <path d="M430,205 C560,170 660,160 809,168 L809,152 C660,144 560,155 430,192 Z" fill="var(--blue-wave)"/>
    <ellipse cx="605" cy="187" rx="174" ry="55" fill="var(--yellow-bright)" stroke="var(--ink)" stroke-width="1.5"/>
    <rect x="0" y="425" width="809" height="113" fill="var(--white)"/>
  </svg>

  <h1 class="abs headline">Got Dirty Printer?</h1>
  <p class="abs badge-text">Get a technician<br>in your office<br>today</p>
  <p class="abs promo promo--front">Also check out our unbeatable<br>Ink and Toner online prices</p>
  <p class="abs display call-label call-label--front">Call today:</p>
  <p class="abs display phone phone--front">718-555-0142</p>
  <p class="abs display visit-label">VISIT US. ONLINE</p>
  <p class="abs display web">WWW.ROWANGOODS.COM</p>
  <div class="abs brand brand--front"><span class="brand__mark"></span>Rowan Office Goods LLC</div>
</section>

<section class="card card--back">
  <svg class="art" width="809" height="538" viewBox="0 0 809 538">
    <defs>
      <linearGradient id="photoToneBack" x1="0" y1="0" x2="1" y2="1">
        <stop offset="0" stop-color="var(--photo-a)"/>
        <stop offset="1" stop-color="var(--photo-b)"/>
      </linearGradient>
    </defs>
    <g role="img" aria-label="Photo of an opened printer mechanism on a repair bench">
      <path d="M0,0 L384,0 L345,140 C325,205 300,232 250,232 L0,232 Z" fill="url(#photoToneBack)" stroke="var(--stamp)" stroke-width="3"/>
    </g>
  </svg>

  <div class="abs stamp"></div>
  <div class="abs brand brand--back"><span class="brand__mark"></span>Rowan Office Goods LLC</div>
  <p class="abs promo promo--back">Also check out our unbeatable<br>Ink and Toner online prices</p>
  <p class="abs display call-label call-label--back">Call today:</p>
  <p class="abs display phone phone--back">718-555-0142</p>
  <div class="abs address-line" style="top:350px"></div>
  <div class="abs address-line" style="top:394px"></div>
  <div class="abs address-line" style="top:439px"></div>
  <div class="abs display footer-band">VISIT US. ONLINE : WWW.ROWANGOODS.COM</div>
</section>

</body>
</html>
```